Bottleless water coolers brochure

We need a flyer for our bottleless water coolers business. The machines connect with a regular water line from a faucet. We use a five filter 9 stage system to provide the absolute best quality water and save money. Our clients (right now we try and focus only on commercial ones) rent our machines for a monthly fee and the get: free installation, filter change every six months. We want people to replace the 5 gallon jug, with our machines. Benefits: constant water flow, frees up space, you don't have to call for water delivery nor have the guy coming in and out of the office with the water jugs. So we probably want to have a jug with the red "do not..." circle around it so people know what it means easily.
Our supplier is frestavo.com if you want to check it out to get an idea of what we offer and our machines.
Our email ops@zelmovendpr.com tel 787-552-6031. We also offer a free trial of one week. If you need other files I should be able to get them. The brochure should be letter size, landscape and foldable.
We are a small vending machine company in Puerto Rico that is starting in bottleless coolers and single serve coffee (kcups).
Our competition in water is brookpuremx.com.
We want something professional yet not dull looking.
Target Market(s)
business owners and companies
Industry/Entity Type
Business
Look and feel

```html
<!DOCTYPE html>
<html lang="es">
<head>
<meta charset="utf-8">
<title>Zelmo Healthy Vending – Brochure</title>
<link href="https://fonts.googleapis.com/css2?family=Poppins:wght@400;500;600;700&display=swap" rel="stylesheet">
<style>
  :root{
    --bg:#262626;
    --orange:#e05a0e;
    --green:#8dc031;
    --green-dark:#6f9e1f;
    --blue:#0e5285;
    --ink-blue:#1d4f8f;
    --white:#ffffff;
  }
  *{margin:0;padding:0;box-sizing:border-box}
  html,body{width:1200px;height:900px;overflow:hidden;background:var(--bg);font-family:"Poppins",sans-serif}
  .brochure{position:absolute;left:30px;top:46px;width:1140px;height:808px;overflow:hidden;box-shadow:0 10px 30px rgba(0,0,0,.5)}
  .panel{position:absolute;top:0;height:808px;width:380px}
  .panel--benefits{left:0;background:var(--orange)}
  .panel--contact{left:380px;background:var(--green)}
  .panel--cover{left:760px;background:var(--blue)}
  .hero{position:absolute;left:0;top:0;width:1140px;height:808px;pointer-events:none}

  .benefits-banner{position:absolute;left:14px;top:71px;width:350px;height:62px}
  .benefits-banner svg{position:absolute;inset:0}
  .benefits-banner h2{position:relative;color:var(--white);font-weight:700;font-size:18px;line-height:22px;text-align:center;padding:9px 40px 0 32px}
  .benefit-list{position:absolute;left:28px;top:166px;width:330px;list-style:none}
  .benefit-list li{position:relative;padding-left:22px;color:var(--white);font-size:14.5px;line-height:17px;margin-bottom:13px}
  .benefit-list li::before{content:"";position:absolute;left:0;top:3px;width:10px;height:10px;border-radius:50%;border:3px solid var(--white);border-top-color:var(--green)}
  .benefit-list li:nth-child(odd)::before{border-color:var(--green);border-top-color:var(--white)}
  .cta{position:absolute;left:0;top:482px;width:380px;text-align:center;color:var(--white);font-weight:700;font-size:21px;line-height:25px}
  .trial{position:absolute;left:48px;top:612px;color:var(--white);font-weight:700;font-size:31px;line-height:34px}
  .trial .free{display:block;color:var(--green);font-size:50px;line-height:54px}
  .trial .of{font-size:18px;font-weight:500}
  .product-shot{position:absolute;left:245px;top:605px;width:125px;height:170px;background:linear-gradient(160deg,#c9ccd0,#6d7177 60%,#3b3e42);border-radius:6px}

  .brand{position:absolute;width:380px;text-align:center;color:var(--white);font-weight:500;letter-spacing:1px}
  .panel--contact .brand{top:540px;font-size:31px}
  .panel--cover .brand{top:594px;font-size:29px}
  .brand small{display:block;font-size:13px;letter-spacing:3px;margin-top:-4px}
  .contact-list{position:absolute;left:60px;top:636px;list-style:none}
  .contact-list li{position:relative;padding-left:38px;color:var(--ink-blue);font-weight:500;font-size:18px;line-height:22px;margin-bottom:14px}
  .contact-list .icon{position:absolute;left:0;top:0;width:24px;height:24px}
  .cover-contact{position:absolute;left:0;top:650px;width:380px;text-align:center;color:var(--white);font-weight:500;font-size:18px;line-height:22px}
  .cover-contact svg{display:block;margin:0 auto 6px}
  .cover-contact p{margin-bottom:10px}
</style>
</head>
<body>
<main class="brochure">
  <section class="panel panel--benefits">
    <div class="benefits-banner">
      <svg width="350" height="62" viewBox="0 0 350 62"><path d="M0,31 L30,0 L30,6 L320,6 L320,0 L350,31 L320,62 L320,56 L30,56 L30,62 Z" fill="var(--green)"/></svg>
      <h2>Modernas máquinas de agua sin botellón Beneficios:</h2>
    </div>
    <ul class="benefit-list">
      <li>Ahorre dinero $$$. Los mejores precios en el mercado.</li>
      <li>Sistema de 9 filtros, garantizando agua siempre fresca .</li>
      <li>Cambio de filtro cada 6 meses gratis.</li>
      <li>Reemplazo de equipo por imperfectos.</li>
      <li>Sin BPAs.</li>
      <li>Instalación gratuita hasta 30'.</li>
    </ul>
    <p class="cta">VENDING. CAFÉ.<br>MAQUINAS DE AGUA SIN<br>BOTELLON ESCRIBENOS!</p>
    <p class="trial"><span class="free">Free</span>trial <span class="of">of</span><br>one week.</p>
    <div class="product-shot" role="img" aria-label="Photo of a silver countertop bottleless water cooler"></div>
  </section>

  <section class="panel panel--contact">
    <p class="brand">ZELMO<small>HEALTHY VENDING</small></p>
    <ul class="contact-list">
      <li><svg class="icon" viewBox="0 0 24 24"><circle cx="12" cy="12" r="10.5" fill="none" stroke="#fff" stroke-width="2"/><path d="M9 6.5l2 3-1.3 1.2c.6 1.5 1.6 2.6 3 3.2L14 12.6l3 2-1 2.2c-4.5-.3-8.3-4-8.6-8.6z" fill="#fff"/></svg>787-552-6031</li>
      <li><svg class="icon" viewBox="0 0 24 24"><circle cx="12" cy="12" r="10.5" fill="none" stroke="#fff" stroke-width="2"/><circle cx="12" cy="12" r="5" fill="none" stroke="#fff" stroke-width="1.6"/><path d="M7 12h10M12 7v10" stroke="#fff" stroke-width="1.2"/></svg>http://www.zelmovendpr.com</li>
      <li><svg class="icon" viewBox="0 0 24 24"><circle cx="12" cy="12" r="10.5" fill="none" stroke="#fff" stroke-width="2"/><path d="M12 6a4 4 0 0 1 4 4c0 3-4 8-4 8s-4-5-4-8a4 4 0 0 1 4-4z" fill="#fff"/></svg>14 Calle Marina, Suite B,<br>Ponce, PR 00716</li>
    </ul>
  </section>

  <section class="panel panel--cover">
    <p class="brand">ZELMO<small>HEALTHY VENDING</small></p>
    <div class="cover-contact">
      <svg width="16" height="16" viewBox="0 0 24 24"><circle cx="12" cy="12" r="12" fill="#fff"/><circle cx="12" cy="12" r="5" fill="none" stroke="var(--blue)" stroke-width="2"/></svg>
      <p>http://www.zelmovendpr.com</p>
      <svg width="16" height="16" viewBox="0 0 24 24"><circle cx="12" cy="12" r="12" fill="#fff"/><path d="M9 6.5l2 3-1.3 1.2c.6 1.5 1.6 2.6 3 3.2L14 12.6l3 2-1 2.2c-4.5-.3-8.3-4-8.6-8.6z" fill="var(--blue)"/></svg>
      <p>787-552-6031</p>
    </div>
  </section>

  <svg class="hero" viewBox="0 0 1140 808">
    <defs>
      <linearGradient id="photoIndoor" x1="0" y1="0" x2="1" y2="1"><stop offset="0" stop-color="#f2f2f0"/><stop offset=".6" stop-color="#c9b7a8"/><stop offset="1" stop-color="#9fb6c6"/></linearGradient>
      <linearGradient id="photoOutdoor" x1="0" y1="0" x2="1" y2="1"><stop offset="0" stop-color="#7f8f5e"/><stop offset=".55" stop-color="#b59a82"/><stop offset="1" stop-color="#5d6b45"/></linearGradient>
      <clipPath id="photoArea"><path d="M394,0 L1140,0 L1140,300 L760,375 C580,385 430,260 394,0 Z"/></clipPath>
    </defs>
    <path d="M380,0 L394,0 C430,260 580,385 760,375 L1060,322 L1052,292 L1140,318 L1082,438 L1074,408 L800,478 C560,505 398,320 380,0 Z" fill="var(--green)"/>
    <g clip-path="url(#photoArea)">
      <rect x="394" y="0" width="366" height="400" fill="url(#photoIndoor)" role="img" aria-label="Photo of a smiling woman holding a glass of water indoors"/>
      <rect x="760" y="0" width="380" height="400" fill="url(#photoOutdoor)" role="img" aria-label="Photo of a woman drinking a glass of water outdoors among trees"/>
    </g>
    <path d="M394,0 C430,260 580,385 760,375 L1140,300" fill="none" stroke="#fff" stroke-width="6"/>
  </svg>
</main>
</body>
</html>
```